Ren2Sue Sign

Sign will be used to advertise my personal injury law firm. Sign will be 4' x 8'. With that in mind, I want it to pop, but not too busy. I have two logos I use, so feel free to incorporate either of those. I have attached a couple photos of me to choose from, the two logos (use one if it fits), and I want the sign to say something to the effect of "Car Accident?" Call me. Ask for Ren. 866-REN2SUE." I have also attached a sign design that I had made on another project. Feel free to use for inspiration.
Updates

I appreciate all the designs, but pretty much every one looks the same. I was hoping for some variety. It looks like most of the designers are using the same template. I know the sign is small, so it doesn't allow for much. But I have updated my "brief" and included some examples of signs that stood out to me. Hope this helps.

Requirements
Must have
• Car Accident?
Call me. Ask for Ren.
866-REN2SUE
Veteran Owned
Photo of me
Nice to have
• My Ren2Sue logo

```html
<!DOCTYPE html>
<html lang="en">
<head>
<meta charset="utf-8">
<title>Ren2Sue Sign</title>
<link rel="stylesheet" href="https://fonts.googleapis.com/css2?family=Oswald:wght@700&family=Tinos:wght@400;700&family=Montserrat:wght@700&display=swap">
<style>
  :root {
    --green: #2f5a2c;
    --teal: #155e72;
    --ink: #2d2d2d;
    --paper: #ffffff;
    --backdrop: #e6e6e6;
    --photo-light: #bdbdbd;
    --photo-dark: #3a3a3a;
  }
  html, body {
    margin: 0;
    width: 1120px;
    height: 1200px;
    overflow: hidden;
    background: var(--backdrop);
  }
  .sign {
    position: absolute;
    left: 40px;
    top: 340px;
    width: 1040px;
    height: 520px;
    background: var(--paper);
    overflow: hidden;
    box-shadow: 0 10px 30px rgba(0,0,0,.18);
  }
  .headline {
    position: absolute;
    margin: 0;
    font-family: "Oswald", sans-serif;
    font-weight: 700;
    font-size: 150px;
    line-height: 1;
    letter-spacing: -3px;
  }
  .headline--car { left: 46px; top: 22px; color: var(--green); }
  .headline--accident { left: 426px; top: 22px; color: var(--teal); }
  .portrait {
    position: absolute;
    left: 105px;
    top: 15px;
    width: 483px;
    height: 505px;
  }
  .veteran {
    position: absolute;
    left: 50px;
    top: 203px;
    width: 138px;
    text-align: center;
  }
  .veteran__mark {
    display: block;
    width: 136px;
    height: 68px;
    background: var(--teal);
  }
  .veteran__label {
    display: block;
    margin-top: 8px;
    font-family: "Montserrat", sans-serif;
    font-weight: 700;
    font-size: 16px;
    color: #111;
  }
  .call-banner {
    position: absolute;
    left: 560px;
    top: 220px;
    width: 437px;
    height: 46px;
  }
  .call-banner svg { position: absolute; inset: 0; }
  .call-banner__text {
    position: absolute;
    right: 16px;
    top: 3px;
    margin: 0;
    font-family: "Tinos", serif;
    font-weight: 700;
    font-size: 34px;
    line-height: 40px;
    color: var(--paper);
    letter-spacing: 0.5px;
  }
  .phone {
    position: absolute;
    right: 44px;
    top: 276px;
    margin: 0;
    font-family: "Oswald", sans-serif;
    font-weight: 700;
    font-size: 84px;
    line-height: 1;
    color: var(--ink);
    letter-spacing: -1px;
  }
  .phone__accent { color: var(--teal); }
  .firm-name {
    position: absolute;
    right: 48px;
    top: 384px;
    margin: 0;
    font-family: "Tinos", serif;
    font-weight: 400;
    font-size: 82px;
    line-height: 1;
    color: var(--green);
  }
</style>
</head>
<body>
  <main class="sign">
    <h1 class="headline headline--car">Car</h1>
    <h1 class="headline headline--accident">Accident?</h1>

    <svg class="portrait" role="img" aria-label="Black and white portrait of the attorney in a suit jacket and open-collar shirt" viewBox="0 0 483 505">
      <defs>
        <linearGradient id="portraitTone" x1="0" y1="0" x2="0" y2="1">
          <stop offset="0" stop-color="var(--photo-dark)"/>
          <stop offset="0.45" stop-color="var(--photo-light)"/>
          <stop offset="1" stop-color="var(--photo-dark)"/>
        </linearGradient>
      </defs>
      <path d="M149 70 Q149 0 229 0 Q309 0 309 70 L309 250 Q420 270 460 330 L483 505 L0 505 L20 330 Q60 270 149 250 Z" fill="url(#portraitTone)"/>
    </svg>

    <div class="veteran">
      <span class="veteran__mark"></span>
      <span class="veteran__label">Veteran Owned</span>
    </div>

    <div class="call-banner">
      <svg viewBox="0 0 437 46" width="437" height="46" aria-hidden="true">
        <polygon points="28,0 437,0 437,46 0,46" fill="var(--green)"/>
      </svg>
      <p class="call-banner__text">Call me. Ask for Ren.</p>
    </div>

    <p class="phone">866-REN<span class="phone__accent">2</span>SUE</p>

    <p class="firm-name">Ren2Sue</p>
  </main>
</body>
</html>
```